Design Creative Banner or Gif Ads. 3 Designs To Be Selected

Come up with some creative banner ads for stonewell.co.nz

*At least 3 different winning banners will be chosen*

Please provide banner ads / gif ads in common google ads / website banner formats.

They can be gif or static but must stand out while still maintaining clear clean text and visuals, with a premium professional feel (please avoid clip art or anything that gives a cheap message).

Please keep in mind that these will likely be small ads so text needs to be large and if there's there a lot of text then use multiple frames/ pages as submit as a gif.

Style
Minimal & clean lines
Architectural or realistic images
Avoid cartoon styles, clipart, or anything that looks cheap

Font
Nexa or Montserrat or similar

Tone
Premium, serious, trustworthy — fits new builds

Colours
Option 1: Deep Navy (trust & quality) & lighter blues and warm grey
Option 2: Open to bright colours to help the ads stand out, such as (but not limited to) bright pink with black, yellow, fluorescent green, provided the messaging is still done professionally.
Our logo is attached (Stone Well Logo)

Display Sizes
Ad specs for file sizes should be file formats like JPEG, GIF, and PNG, with animations limited to a max of 30 seconds or less.
We will need several different ad sizes provided for each of the 3 selected winning designs.

• Medium Rectangle: 300 × 250 pixels
• Leaderboard: 728 × 90 pixels
• Desktop Banner ad image: (640x360 pixels)
• Desktop Banner ad image 2: (300x600 pixels)
• Possibly one or two other sizes

Flexibility to be creative
The ad text, words, upper/lower case, layout, colour, theme, and images can be adjusted to how you think it will look best. The follow example ads are just examples of what we are after but we are keen to see what you can create.

Recommendations at this point:
1. Avoid text heavy
2. Looking for more Gif ads
3. Imaging: if possible use real stock photo's rather than AI

Themes:

1
Building Soon? Start Here
Free Build Planning Pack:
✓ Build Cost Calculator
✓ Hidden Cost Checklist
✓ Builder Comparison Guide
Build With Confidence
Download Free

2
Before You Choose A Builder
Compare Price, Scope, Risk & Value
Avoid Costly Mistakes
Choose The Right Builder With Confidence
Download The Free Guide

3
Planning A New Build?
Avoid These Common Mistakes:
✗ Hidden Exclusions
✗ Missing Scope
✗ Unrealistic Allowances
✗ Budget Blowouts
Download The Free Guide

4
Before You Buy Land
Know what it could cost to build.
Avoid Costly Building Mistakes
Download Our Free Guides

5
Know Your Build Budget?
• Free Build Cost Calculator
• Hidden Cost Checklist
• Build Planning Tools
Calculate Costs (Download)

Target Market(s)

Landowners looking to build

Industry/Entity Type

Building

Font styles to use
Other font styles liked:
• Nexa or Montserrat or similar

Requirements
Should not have
• Avoid cartoon styles, clipart, or anything that looks cheap

```html
<!DOCTYPE html>
<html lang="en">
<head>
<meta charset="utf-8">
<title>Stone Well – Free Build Planning Pack</title>
<link href="https://fonts.googleapis.com/css2?family=Montserrat:wght@500;600;700;800;900&display=swap" rel="stylesheet">
<style>
  :root {
    --navy-deep: #07111f;
    --navy: #0c1b31;
    --navy-mid: #132a48;
    --blue-accent: #2f8fc9;
    --blue-light: #4aa6db;
    --white: #ffffff;
    --grey-band: #eceef1;
    --grey-text: #1b2433;
    --divider: rgba(255,255,255,0.18);
  }
  * { margin: 0; padding: 0; box-sizing: border-box; }
  html, body { width: 1200px; height: 266px; overflow: hidden; background: var(--navy-deep); }
  body { font-family: "Montserrat", sans-serif; }

  .banner {
    position: relative;
    width: 1200px;
    height: 266px;
    overflow: hidden;
    background: linear-gradient(100deg, var(--navy-deep) 0%, var(--navy) 45%, var(--navy-mid) 75%, var(--navy) 100%);
  }

  .brand {
    position: absolute;
    left: 43px;
    top: 66px;
    width: 115px;
    text-align: center;
    color: var(--white);
  }
  .brand-mark {
    display: block;
    width: 14px;
    height: 14px;
    margin: 0 auto 8px;
    background: var(--white);
  }
  .brand-name {
    font-size: 17px;
    font-weight: 700;
    letter-spacing: 0.2px;
    line-height: 1;
  }
  .brand-tagline {
    margin-top: 4px;
    font-size: 4.6px;
    font-weight: 700;
    letter-spacing: 0.1px;
    text-transform: uppercase;
    white-space: nowrap;
  }

  .headline {
    position: absolute;
    left: 196px;
    top: 38px;
    font-size: 35px;
    font-weight: 900;
    line-height: 34px;
    color: var(--white);
    text-transform: uppercase;
    letter-spacing: -0.3px;
  }
  .headline .accent { color: var(--blue-accent); display: block; }

  .cta {
    position: absolute;
    left: 197px;
    top: 154px;
    width: 232px;
    height: 39px;
    border-radius: 6px;
    background: linear-gradient(90deg, #2a86bd, var(--blue-light));
    color: var(--white);
    display: flex;
    align-items: center;
    justify-content: center;
    gap: 12px;
    font-size: 12.5px;
    font-weight: 700;
    text-transform: uppercase;
    letter-spacing: 0.2px;
  }
  .cta svg { width: 17px; height: 17px; }

  .divider {
    position: absolute;
    left: 546px;
    top: 31px;
    width: 1px;
    height: 190px;
    background: var(--divider);
  }

  .pack {
    position: absolute;
    left: 578px;
    top: 29px;
    color: var(--white);
  }
  .pack-title {
    font-size: 13px;
    font-weight: 800;
    text-transform: uppercase;
    letter-spacing: 0.2px;
    margin-bottom: 12px;
  }
  .pack-list { list-style: none; }
  .pack-item {
    display: flex;
    align-items: center;
    gap: 9px;
    height: 39px;
    margin-bottom: 12px;
  }
  .pack-icon {
    width: 39px;
    height: 39px;
    border-radius: 50%;
    background: linear-gradient(160deg, var(--blue-light), #2478ab);
    display: flex;
    align-items: center;
    justify-content: center;
    flex-shrink: 0;
  }
  .pack-icon svg { width: 21px; height: 21px; }
  .pack-label {
    font-size: 14.5px;
    font-weight: 500;
    line-height: 19px;
  }

  .hero-photo {
    position: absolute;
    left: 735px;
    top: 0;
    width: 465px;
    height: 240px;
    clip-path: polygon(108px 0, 465px 0, 465px 240px, 0 240px);
    background:
      radial-gradient(ellipse at 55% 55%, rgba(236,170,110,0.55) 0%, rgba(236,170,110,0) 45%),
      linear-gradient(180deg, #8fa6c2 0%, #5e7190 35%, #3a3f4a 62%, #2b3a2a 85%, #1d2620 100%);
  }

  .footer-band {
    position: absolute;
    left: 0;
    top: 240px;
    width: 1200px;
    height: 26px;
    background: var(--grey-band);
    color: var(--grey-text);
    font-size: 11.5px;
    font-weight: 600;
  }
  .footer-item {
    position: absolute;
    top: 0;
    height: 26px;
    display: flex;
    align-items: center;
    gap: 6px;
  }
  .footer-item svg { width: 14px; height: 14px; }
  .footer-promise { left: 36px; }
  .footer-site { left: 541px; }
</style>
</head>
<body>
<div class="banner">
  <div class="brand">
    <span class="brand-mark"></span>
    <div class="brand-name">Stone Well</div>
    <div class="brand-tagline">Compare quotes from trusted builders</div>
  </div>

  <h1 class="headline">
    Bought land?
    <span class="accent">Avoid costly</span>
    Build mistakes
  </h1>

  <div class="cta">
    <svg viewBox="0 0 24 24" fill="none" stroke="#fff" stroke-width="2.2" stroke-linecap="round" stroke-linejoin="round"><path d="M12 3v12"/><path d="M7 10l5 5 5-5"/><path d="M4 17v3h16v-3"/></svg>
    Download free guide
  </div>

  <div class="divider"></div>

  <div class="pack">
    <div class="pack-title">Free build planning pack</div>
    <ul class="pack-list">
      <li class="pack-item">
        <span class="pack-icon">
          <svg viewBox="0 0 24 24" fill="none" stroke="#fff" stroke-width="1.8" stroke-linejoin="round"><rect x="5" y="2.5" width="14" height="19" rx="2"/><rect x="8" y="5.5" width="8" height="4"/><path d="M8.5 13h1M12 13h1M15.5 13h0M8.5 16.5h1M12 16.5h1" stroke-linecap="round"/></svg>
        </span>
        <span class="pack-label">Build Cost<br>Calculator</span>
      </li>
      <li class="pack-item">
        <span class="pack-icon">
          <svg viewBox="0 0 24 24" fill="none" stroke="#fff" stroke-width="1.8" stroke-linejoin="round"><path d="M3 6l6-2 6 2 6-2v14l-6 2-6-2-6 2z"/><path d="M9 4v14M15 6v14"/></svg>
        </span>
        <span class="pack-label">Build Journey<br>Roadmap</span>
      </li>
      <li class="pack-item">
        <span class="pack-icon">
          <svg viewBox="0 0 24 24" fill="none" stroke="#fff" stroke-width="1.8" stroke-linecap="round" stroke-linejoin="round"><rect x="5" y="4" width="14" height="17" rx="1.5"/><path d="M9 3h6v3H9z"/><path d="M8 10h8M8 13.5h5"/><path d="M13 18l1.5 1.5L17.5 16"/></svg>
        </span>
        <span class="pack-label">Hidden Cost<br>Checklist</span>
      </li>
    </ul>
  </div>

  <div class="hero-photo" role="img" aria-label="Modern two-storey home with timber cladding and large glass walls, lit warmly at dusk with landscaped garden steps"></div>

  <div class="footer-band">
    <div class="footer-item footer-promise">
      <svg viewBox="0 0 24 24" fill="none" stroke="#1b2433" stroke-width="2" stroke-linecap="round" stroke-linejoin="round"><path d="M12 2.5l8 3v6c0 5-3.5 8.5-8 10-4.5-1.5-8-5-8-10v-6z"/><path d="M8.5 12l2.5 2.5 4.5-5"/></svg>
      Choose The Right Builder With Clarity &amp; Confidence
    </div>
    <div class="footer-item footer-site">
      <svg viewBox="0 0 24 24" fill="#1b2433"><circle cx="12" cy="12" r="10"/><path d="M2 12h20M12 2c3 3 3 17 0 20M12 2c-3 3-3 17 0 20" stroke="#eceef1" stroke-width="1.4" fill="none"/></svg>
      stonewell.co.nz
    </div>
  </div>
</div>
</body>
</html>
```